依頼詳細
現サイト http://www.kazeharuso.jp/

今回のリニューアルでは基調色を「緑以外」というご希望です。
素材は下記からダウンロードしていただけます。
※容量が大きいです。施設パンフなどに使ったものを一切合切入れてあります。

自由な発想でデザインしてみてください。
シンプル系もありだと思います。
サイトURL
http://www.kazeharuso.jp/
ページ数
1ページ
希望イメージ
シンプル 複雑
単色 カラフル
暗い 明るい
日常 高級
遊び心 厳粛
未来的 伝統的
女性的 男性的
希望する色
赤系、水色系、黄・オレンジ系
納品ファイル
• フォトショップ形式 (.psd)
• PNG形式 (.png)
補足説明
サイトマップを添付致します。
★タイトなスケジュールで申し訳ありませんが、ぜひご提案くださいませ。
よろしくお願い致します!
素材のダウンロード先を記入し忘れておりました。申し訳ありません。
https://dl07.filepokku.jp/get/9b3d27a1c6e05f4a8d12b7e93c0fa6d5.html
(パスワード: tonKebaW)
サイトマップの添付を追加致しました。
選定確約という機能があることを知りました。チェックをいれましたので必ず当選者様を選定致します。

sekinohato様
お世話になります。今回のご提案をクライアント様に気に入っていただきました。修正なしでこのままでOKでございます。
シンプル系がやはりクライアント様が選んだ一番の理由だったと思います。
すばらしいです。

弊社判断で当選を決定できなかったのですが、先方クライアント様との打ち合わせで、「おそらくこれが一番気に入られるかな」という印象でした。
昨日、プリントアウトしてプリンターの加減も含めた中で、当選決定となりました。やはりディレクションの重要さとそれをクラウドソーシングに伝える難しさや良さも同時に感じました。
今回は本当にありがとうございます。
株式会社ケト 杉本

```html
<!DOCTYPE html>
<html lang="ja">
<head>
<meta charset="utf-8">
<title>特別養護老人ホーム 風晴荘</title>
<link href="https://fonts.googleapis.com/css2?family=Noto+Sans+JP:wght@400;500;700&family=Noto+Serif+JP:wght@500;700&display=swap" rel="stylesheet">
<style>
:root{
  --orange:#ec6a2f;
  --orange-dark:#d4561d;
  --red:#d8302a;
  --cyan:#36b8e0;
  --green:#39b26b;
  --blue:#1d96dd;
  --ink:#333;
  --grey:#4a4a4a;
  --line:#d9d9d9;
  --white:#fff;
}
*{margin:0;padding:0;box-sizing:border-box}
html,body{width:1200px;height:2964px;overflow:hidden}
body{font-family:"Noto Sans JP",sans-serif;color:var(--ink);background:var(--white);position:relative}

.site-header{height:56px;display:flex;align-items:center;justify-content:space-between;padding:0 24px;background:var(--white)}
.brand-small{display:flex;align-items:center;gap:14px}
.brand-small .org{font-size:12px;line-height:1.3;color:var(--grey)}
.brand-small .name{font-family:"Noto Serif JP",serif;font-weight:700;font-size:28px;color:var(--grey)}
.header-contact{display:flex;align-items:center;gap:18px}
.header-tel{display:flex;align-items:center;gap:8px;font-size:26px;font-weight:500;color:var(--grey)}
.header-btn{background:var(--orange);color:#fff;font-size:16px;padding:8px 18px;border-radius:3px;display:flex;align-items:center;gap:6px}

.hero{height:376px;position:relative;background:linear-gradient(180deg,#9cc6e6 0%,#c7e1f1 30%,#7b9b6a 55%,#8a6a4e 80%,#b9a48a 100%)}
.hero-logo{position:absolute;left:428px;top:120px;width:344px;height:150px;background:rgba(236,106,47,.92);color:#fff;text-align:center;padding-top:18px}
.hero-logo .org{font-size:18px;line-height:1.4;font-family:"Noto Serif JP",serif;font-weight:500}
.hero-logo .name{font-family:"Noto Serif JP",serif;font-weight:500;font-size:54px;line-height:1.2;letter-spacing:6px}

.motto{height:144px;text-align:center;padding-top:28px;font-family:"Noto Serif JP",serif}
.motto .lead{color:var(--red);font-size:27px;font-weight:700}
.motto .sub{color:var(--grey);font-size:19px;margin-top:10px}
.motto .sub em{font-style:normal;color:var(--red);font-weight:700}

.global-nav{display:flex;gap:10px;padding:0 24px;height:72px}
.global-nav a{flex:1;background:var(--orange);color:#fff;text-decoration:none;display:flex;align-items:center;justify-content:center;text-align:center;font-size:19px;font-weight:500;line-height:1.25;border-radius:2px}

.concept{position:absolute;top:680px;left:0;width:1200px;height:480px;background:linear-gradient(160deg,#f2f5e8 0%,#d9e6b8 35%,#eef0e0 60%,#c8d7a0 100%)}
.concept-title{position:absolute;top:46px;width:100%;text-align:center;font-family:"Noto Serif JP",serif;font-size:30px;color:#fff;text-shadow:0 1px 4px rgba(0,0,0,.35)}
.concept-badge{position:absolute;left:620px;top:110px;width:170px;height:170px;border-radius:50%;background:var(--orange);color:#fff;display:flex;align-items:center;justify-content:center;text-align:center;white-space:nowrap;font-family:"Noto Serif JP",serif;font-size:18px;letter-spacing:0}
.concept-text{position:absolute;left:0;right:0;bottom:0;height:196px;background:rgba(40,40,40,.62);color:#fff;font-size:16px;line-height:1.85;text-align:center;padding:26px 80px 0}

.news{position:absolute;top:1180px;left:30px;width:1140px;display:flex;gap:32px}
.news-col{flex:1}
.news-head{height:36px;color:#fff;font-size:18px;font-weight:500;display:flex;align-items:center;justify-content:center}
.news-col.info .news-head{background:var(--cyan)}
.news-col.recruit .news-head{background:var(--green)}
.news-list{list-style:none}
.news-list li{border-bottom:1px solid var(--line);padding:8px 6px;font-size:15px;line-height:1.55;height:64px}
.news-list time{display:block;color:var(--grey)}
.news-more{width:240px;height:46px;margin:26px auto 0;background:var(--grey);color:#fff;font-size:16px;display:flex;align-items:center;justify-content:center;text-decoration:none}

.services{position:absolute;top:1680px;left:0;width:1200px;height:800px;background:linear-gradient(180deg,#d8d2c6 0%,#b8a98f 40%,#cfc5b4 100%)}
.services h2{text-align:center;color:#fff;font-weight:500;font-size:40px;padding-top:44px;text-shadow:0 1px 4px rgba(0,0,0,.35)}
.svc{position:absolute;width:344px;height:224px;border:4px solid rgba(255,255,255,.85);background:rgba(255,255,255,.85)}
.svc .label{height:48px;display:flex;align-items:center;justify-content:center;font-size:20px;color:var(--ink)}
.svc .photo{height:168px}
.facility-link{position:absolute;left:354px;top:618px;width:492px;height:90px;background:rgba(50,50,50,.72);color:#fff;font-family:"Noto Serif JP",serif;font-size:40px;display:flex;align-items:center;justify-content:center;letter-spacing:2px}

.quick-links{position:absolute;top:2484px;left:30px;width:1140px;display:flex;gap:22px}
.quick-links a{flex:1;height:118px;background:var(--blue);color:#fff;text-decoration:none;font-size:34px;display:flex;align-items:center;justify-content:center;gap:16px}

.site-footer{position:absolute;top:2640px;left:0;width:1200px;height:324px;background:var(--orange);color:#fff}
.footer-brand{display:flex;justify-content:center;align-items:center;gap:14px;padding-top:34px}
.footer-brand .org{font-size:16px;line-height:1.35;text-align:right}
.footer-brand .name{font-family:"Noto Serif JP",serif;font-weight:700;font-size:44px}
.footer-address{text-align:center;font-size:16px;margin-top:20px}
.footer-address span{margin:0 18px}
.footer-nav{position:absolute;bottom:0;left:0;right:0;height:76px;border-top:1px solid rgba(255,255,255,.45);display:flex;align-items:center;justify-content:center;gap:48px;font-size:15px}
</style>
</head>
<body>

<header class="site-header">
  <div class="brand-small">
    <div class="org">社会福祉法人 和光会<br>特別養護老人ホーム</div>
    <div class="name">風晴荘</div>
  </div>
  <div class="header-contact">
    <div class="header-tel">
      <svg width="26" height="26" viewBox="0 0 24 24" aria-hidden="true"><path fill="#4a4a4a" d="M6.6 10.8a15.1 15.1 0 0 0 6.6 6.6l2.2-2.2c.3-.3.7-.4 1-.2 1.1.4 2.3.6 3.6.6.6 0 1 .4 1 1V20c0 .6-.4 1-1 1A17 17 0 0 1 3 4c0-.6.4-1 1-1h3.5c.6 0 1 .4 1 1 0 1.2.2 2.4.6 3.6.1.3 0 .7-.2 1z"/></svg>
      0745-00-1234
    </div>
    <div class="header-btn">
      <svg width="16" height="12" viewBox="0 0 16 12" aria-hidden="true"><rect x="0.5" y="0.5" width="15" height="11" fill="none" stroke="#fff"/><path d="M1 1l7 6 7-6" fill="none" stroke="#fff"/></svg>
      お問合せ
    </div>
  </div>
</header>

<section class="hero" role="img" aria-label="山の緑に囲まれた施設の外観写真">
  <div class="hero-logo">
    <div class="org">社会福祉法人 和光会<br>特別養護老人ホーム</div>
    <div class="name">風晴荘</div>
  </div>
</section>

<section class="motto">
  <p class="lead">「相互信頼の心、和を以って楽しい“家族”でありたい」</p>
  <p class="sub">と願う私たちの施設は「<em>風晴荘</em>」と命名されています。</p>
</section>

<nav class="global-nav">
  <a href="#">サービス案内</a>
  <a href="#">施設案内</a>
  <a href="#">施設概要</a>
  <a href="#">社会福祉法人<br>和光会について</a>
  <a href="#">よくある質問</a>
  <a href="#">お問合せ</a>
</nav>

<section class="concept" role="img" aria-label="白い花の写真">
  <p class="concept-title">自然とともに、人とのふれあい励ましあいを大切に</p>
  <div class="concept-badge">ハートフル・ケア</div>
  <div class="concept-text">
    風晴荘は奈良県青葉市の北部、青葉中央駅から約3kmの小高い丘陵地に位置します。<br>
    緑濃く、清澄な空気と四季折々の自然に恵まれ、静かな環境のもと、<br>
    特別養護老人ホームを中心に様々なサービスを提供しています。<br>
    ご利用者の方が、これまでの人生を尊重し、<br>
    安心して楽しい日常をお過ごしいただけるようお手伝いいたします。
  </div>
</section>

<section class="news">
  <div class="news-col info">
    <h3 class="news-head">お知らせ</h3>
    <ul class="news-list">
      <li><time>2016/08/18</time>新しいパンフレットができました。</li>
      <li><time>2016/08/18</time>新しいパンフレットができました。</li>
      <li><time>2016/08/18</time>新しいパンフレットができました。</li>
      <li><time>2016/08/18</time>新しいパンフレットができました。</li>
      <li><time>2016/08/18</time>新しいパンフレットができました。</li>
    </ul>
    <a class="news-more" href="#">お知らせ一覧</a>
  </div>
  <div class="news-col recruit">
    <h3 class="news-head">採用情報</h3>
    <ul class="news-list">
      <li><time>2016/08/18</time>新しいパンフレットができました。</li>
      <li><time>2016/08/18</time>新しいパンフレットができました。</li>
      <li><time>2016/08/18</time>新しいパンフレットができました。</li>
      <li><time>2016/08/18</time>新しいパンフレットができました。</li>
      <li><time>2016/08/18</time>新しいパンフレットができました。</li>
    </ul>
    <a class="news-more" href="#">求人のお知らせ</a>
  </div>
</section>

<section class="services" role="img" aria-label="施設内の明るい廊下の写真">
  <h2>サービス案内</h2>
  <div class="svc" style="left:40px;top:126px"><div class="label">特別養護老人ホーム</div><div class="photo" role="img" aria-label="居室の写真" style="background:linear-gradient(135deg,#e9e1d2,#c9b89a)"></div></div>
  <div class="svc" style="left:428px;top:126px"><div class="label">ショートステイ</div><div class="photo" role="img" aria-label="食堂の写真" style="background:linear-gradient(135deg,#d6e0e6,#a9b7b8)"></div></div>
  <div class="svc" style="left:816px;top:126px"><div class="label">デイサービス</div><div class="photo" role="img" aria-label="デイサービス室の写真" style="background:linear-gradient(135deg,#ece6da,#bfae90)"></div></div>
  <div class="svc" style="left:234px;top:366px"><div class="label">居宅介護支援センター</div><div class="photo" role="img" aria-label="相談室の写真" style="background:linear-gradient(135deg,#e7ebe8,#b7c3bd)"></div></div>
  <div class="svc" style="left:622px;top:366px"><div class="label">支援ハウス</div><div class="photo" role="img" aria-label="支援ハウス外観の写真" style="background:linear-gradient(135deg,#dbe8f0,#9fb48a)"></div></div>
  <a class="facility-link">風晴荘 施設案内</a>
</section>

<nav class="quick-links">
  <a href="#"><svg width="44" height="44" viewBox="0 0 44 44" aria-hidden="true"><circle cx="22" cy="22" r="19" fill="none" stroke="#fff" stroke-width="4"/><path d="M16 17a6 6 0 1 1 8 5.6c-1.4.6-2 1.6-2 3v1.4" fill="none" stroke="#fff" stroke-width="4"/><circle cx="22" cy="32.5" r="2.4" fill="#fff"/></svg>よくある質問</a>
  <a href="#"><svg width="50" height="36" viewBox="0 0 50 36" aria-hidden="true"><rect x="2" y="2" width="46" height="32" fill="none" stroke="#fff" stroke-width="4"/><path d="M3 3l22 18L47 3" fill="none" stroke="#fff" stroke-width="4"/></svg>お問合せ</a>
  <a href="#"><svg width="54" height="40" viewBox="0 0 54 40" aria-hidden="true"><path d="M4 20l6-14h34l6 14v12H4z" fill="#fff"/><rect x="13" y="9" width="28" height="10" fill="#1d96dd"/><circle cx="14" cy="33" r="6" fill="#fff" stroke="#1d96dd" stroke-width="3"/><circle cx="40" cy="33" r="6" fill="#fff" stroke="#1d96dd" stroke-width="3"/></svg>アクセス</a>
</nav>

<footer class="site-footer">
  <div class="footer-brand">
    <div class="org">社会福祉法人 和光会<br>特別養護老人ホーム</div>
    <div class="name">風晴荘</div>
  </div>
  <p class="footer-address"><span>〒633-0000</span><span>奈良県青葉市若草町1-2-3</span><span>TEL：0745-00-1234</span><span>FAX：0745-00-1235</span></p>
  <nav class="footer-nav">
    <span>トップページ</span><span>サービス案内</span><span>施設案内</span><span>施設概要</span><span>社会福祉法人 和光会について</span><span>よくある質問</span><span>お問合せ</span>
  </nav>
</footer>

</body>
</html>
```